Landing page design for a tech event

A landing page for my event for marketing & business professionals to learn the latest digital contents driven marketing by Quorvel an open source CMS. We need a full web design and code for this responsive landing page.

I would like to have a simple, big UI, flat design and fast loading design with minimum set of color (like B&W + One) but with very audacious creative concept to get people's attention and let them focus on contents.

Target Market(s)

Marketing managers in mid-large enterprises.

Industry/Entity Type

Information Technology

Coding

Coded - Design and coding required

Number of Pages Required

1 page

Font styles to use
Sans Serif

Colors
333333
5c5c5c
9d9d9d
d9d9d9
eeeeee
9bcb3b
add136
cadf82
eaf2ce

Requirements
Must have
• 1. A responsive landing page to promote a tech event with ridiculously good looking creative.
• 2. The landing page must have PC and Smart Phones design as responsive web.
• 3. The landing page must have header menu, top section, about section, program & speakers section, tickets information section, sponsors section, contact section and venue (address & map) section and footer.
• 4. The landing page must have our logo (attached)
• 5. For ticket information section, we will add a widget (attached) from Lantomi.com for ticket sales.
• 6. My request is for you to design an English page but we will use exact same design for Japanese contents as well. so at the end of day, there will be two pages and we need a button to switch page (language) in the header menu.
• 7. Full set of code HTML/CSS/JS.
Nice to have
• Inspirational websites are here.
• For creative:
• http://ateliervortane.com/
• http://www.cruzelmdale.com/
• http://www.plonkit.com/band/
• For contents
• http://meets.dravonhub.com/kx2015/
• http://www.weavebuildpacifica.com
Should not have
• More than one page! ;-)

```html
<!DOCTYPE html>
<html lang="en">
<head>
<meta charset="utf-8">
<title>NEXORA Sydney 2015 – Tech Conference</title>
<link href="https://fonts.googleapis.com/css2?family=Open+Sans:ital,wght@0,400;0,600;0,700;0,800;1,400&display=swap" rel="stylesheet">
<style>
:root{
  --ink:#333333;
  --ink-mid:#5c5c5c;
  --ink-soft:#9d9d9d;
  --line:#d9d9d9;
  --paper:#eeeeee;
  --green:#9bcb3b;
  --green-bright:#add136;
  --green-pale:#cadf82;
  --green-wash:#eaf2ce;
  --night:#222222;
  --white:#ffffff;
}
*{box-sizing:border-box;margin:0;padding:0}
html,body{width:1200px;height:3508px;overflow:hidden}
body{font-family:"Open Sans",Arial,sans-serif;color:var(--ink);background:var(--white);position:relative}
section,header,footer{position:absolute;left:0;width:1200px}

/* Hero */
.hero{top:0;height:820px;overflow:hidden}
.hero-photo{position:absolute;inset:0;background:linear-gradient(180deg,#4a4a4a 0%,#7a7a7a 35%,#8d8d8d 60%,#3c3c3c 100%)}
.hero-shade{position:absolute;inset:0;background:radial-gradient(ellipse at 50% 45%,rgba(255,255,255,.18),rgba(0,0,0,.25) 70%)}
.brand{position:absolute;top:18px;left:0;width:100%;text-align:center}
.brand-name{display:inline-flex;align-items:center;gap:10px;font-size:44px;font-weight:800;color:var(--white);letter-spacing:2px}
.brand-name .dot{width:14px;height:14px;background:var(--green)}
.main-nav{position:absolute;top:104px;left:0;width:100%;display:flex;justify-content:center;gap:56px}
.main-nav a{color:var(--white);font-size:15px;text-decoration:none;font-weight:600}
.hero-title{position:absolute;top:270px;width:100%;text-align:center;color:var(--white);font-size:62px;line-height:66px;font-weight:800}
.hero-tagline{position:absolute;top:412px;width:100%;text-align:center;color:var(--white);font-size:26px;font-weight:700;letter-spacing:.5px}
.hero-date{position:absolute;top:450px;width:100%;text-align:center;color:var(--white);font-size:15px;font-weight:600;letter-spacing:1px}
.hero-cta{position:absolute;top:498px;left:370px;width:460px;height:96px;background:#111;color:var(--white);font-size:24px;line-height:30px;font-weight:800;text-align:center;display:flex;align-items:center;justify-content:center;text-transform:uppercase;white-space:nowrap}

/* Why attend */
.why{top:820px;height:500px;background:var(--paper)}
.section-title{position:absolute;width:100%;text-align:center;font-size:20px;font-weight:700;color:var(--ink-mid);text-transform:uppercase}
.why .section-title{top:28px}
.feature{position:absolute;width:230px;text-align:center}
.feature-icon{display:block;margin:0 auto 12px}
.feature h3{font-size:17px;font-weight:600;color:var(--ink-mid);text-transform:uppercase;margin-bottom:8px}
.feature h3.accent{color:var(--green)}
.feature p{font-size:11.5px;line-height:17px;color:var(--ink-soft)}

/* Video */
.expect{top:1320px;height:660px;background:linear-gradient(160deg,#e6e6e6 0%,#d6d6d6 50%,#cfcfcf 100%)}
.expect .section-title{top:30px}
.monitor{position:absolute;left:250px;top:90px}

/* Speakers */
.speakers{top:1980px;height:520px;background:var(--white)}
.speakers .section-title{top:28px}
.speaker{position:absolute;top:80px;width:200px;text-align:center}
.speaker-photo{width:200px;height:260px;background:linear-gradient(180deg,#d2d2d2,#8e8e8e)}
.speaker-name{margin-top:12px;font-size:12px;font-weight:700;color:var(--ink)}
.speaker-role{font-size:11px;color:var(--ink-soft)}
.more-speakers{position:absolute;top:424px;left:425px;width:350px;height:52px;background:var(--green);color:var(--white);font-size:24px;font-weight:700;text-align:center;line-height:52px}
.more-speakers em{font-weight:400}

/* Location */
.location{top:2500px;height:380px;overflow:hidden}
.location-photo{position:absolute;inset:0;background:linear-gradient(180deg,#bdbdbd 0%,#9a9a9a 55%,#6f6f6f 100%)}
.location-title{position:absolute;top:26px;width:100%;text-align:center;color:var(--white);font-size:15px;font-weight:700;letter-spacing:1px}
.venue-card{position:absolute;top:70px;left:330px;width:540px;height:170px;background:rgba(238,238,238,.88);text-align:center;padding-top:30px}
.venue-card h3{font-size:24px;font-weight:600;color:var(--ink);margin-bottom:14px}
.venue-card p{font-size:14px;line-height:22px;color:var(--ink-mid)}
.venue-btn{position:absolute;top:262px;left:480px;width:240px;height:48px;border:2px solid var(--white);color:var(--white);font-size:15px;font-weight:700;text-align:center;line-height:44px;letter-spacing:1px}

/* Sponsors */
.sponsors{top:2880px;height:320px;background:var(--white)}
.sponsors .section-title{top:24px;color:var(--ink)}
.sponsor-tabs{position:absolute;top:72px;left:0;width:100%;display:flex;justify-content:center}
.sponsor-tabs span{font-size:12px;color:var(--ink-soft);padding:6px 18px;border-right:1px solid var(--line)}
.sponsor-tabs span:last-child{border-right:0}
.sponsor-tabs .active{border:1px solid var(--ink-soft);color:var(--ink)}
.sponsor-row{position:absolute;left:180px;width:840px;display:flex;justify-content:space-between;align-items:center}
.sponsor-mark{display:inline-flex;align-items:center;gap:8px;font-size:24px;font-weight:700;color:var(--ink)}
.sponsor-mark i{display:inline-block;width:18px;height:18px;background:var(--ink)}

/* Footer */
.site-footer{top:3200px;height:308px;background:var(--night);color:var(--ink-soft)}
.footer-col{position:absolute;top:28px}
.footer-col h4{font-size:12px;font-weight:700;color:var(--white);text-transform:uppercase;margin-bottom:12px}
.footer-col p,.footer-col li{font-size:11px;line-height:18px;list-style:none}
.register-btn{display:block;margin-top:6px;width:170px;height:44px;border:2px solid var(--white);color:var(--white);font-size:18px;font-weight:600;text-align:center;line-height:40px}
.copyright{position:absolute;bottom:14px;width:100%;text-align:center;font-size:10px;color:var(--ink-mid)}
</style>
</head>
<body>

<header class="hero">
  <div class="hero-photo" role="img" aria-label="Black and white photo of a festival crowd with raised hands"></div>
  <div class="hero-shade"></div>
  <div class="brand"><span class="brand-name"><span class="dot"></span>NEXORA</span></div>
  <nav class="main-nav">
    <a href="#about">About</a><a href="#speakers">Programs &amp; Speakers</a><a href="#tickets">Get Tickets</a><a href="#sponsors">Sponsors</a><a href="#contact">Contact</a><a href="#venue">Venue</a>
  </nav>
  <h1 class="hero-title">THE FIRST HI TECH NEXORA<br>IN SYDNEY</h1>
  <p class="hero-tagline">CONNECTING ASIA TECH WORLD</p>
  <p class="hero-date">6 - 7 MAY 2015 &nbsp;|&nbsp; HARBOURLINE CONVENTION AND EXHIBITION CENTRE</p>
  <a class="hero-cta">Get your<br>conference passes today</a>
</header>

<section class="why" id="about">
  <h2 class="section-title">Why should you attend?</h2>

  <div class="feature" style="left:193px;top:90px">
    <svg class="feature-icon" width="56" height="56" viewBox="0 0 56 56"><circle cx="28" cy="28" r="28" fill="var(--green)"/><rect x="17" y="19" width="22" height="16" fill="none" stroke="#fff" stroke-width="2.5"/><path d="M22 40h12" stroke="#fff" stroke-width="2.5"/></svg>
    <h3>Arena</h3>
    <p>We cover the entire Asian region and pick the top 10 startups to compete in Arena. The final battle will take place live on the Main stage on Thursday 7 May. Applications are still open!</p>
  </div>
  <div class="feature" style="left:485px;top:90px">
    <svg class="feature-icon" width="56" height="56" viewBox="0 0 56 56"><circle cx="28" cy="28" r="28" fill="var(--green)"/><path d="M18 20h20v16H18z M18 26h20" fill="none" stroke="#fff" stroke-width="2.5"/></svg>
    <h3 class="accent">Bootstrap Alley</h3>
    <p>We cover the entire Asian region and pick the top 10 startups to compete in Arena. The final battle will take place live on the Main stage on Thursday 7 May. Applications are still open!</p>
  </div>
  <div class="feature" style="left:777px;top:90px">
    <svg class="feature-icon" width="56" height="56" viewBox="0 0 56 56"><circle cx="28" cy="28" r="28" fill="var(--green)"/><path d="M17 36l8-9 6 5 8-12" fill="none" stroke="#fff" stroke-width="2.5"/></svg>
    <h3>Night Crawl</h3>
    <p>We cover the entire Asian region and pick the top 10 startups to compete in Arena. The final battle will take place live on the Main stage on Thursday 7 May. Applications are still open!</p>
  </div>

  <div class="feature" style="left:193px;top:290px">
    <svg class="feature-icon" width="56" height="56" viewBox="0 0 56 56"><circle cx="28" cy="28" r="27" fill="var(--white)" stroke="var(--green)" stroke-width="2"/><rect x="18" y="20" width="20" height="14" fill="none" stroke="var(--green)" stroke-width="2"/><path d="M23 38h10" stroke="var(--green)" stroke-width="2"/></svg>
    <h3>Arena</h3>
    <p>We cover the entire Asian region and pick the top 10 startups to compete in Arena. The final battle will take place live on the Main stage on Thursday 7 May. Applications are still open!</p>
  </div>
  <div class="feature" style="left:485px;top:290px">
    <svg class="feature-icon" width="56" height="56" viewBox="0 0 56 56"><circle cx="28" cy="28" r="27" fill="var(--white)" stroke="var(--green)" stroke-width="2"/><path d="M19 21h18v14H19z M19 26h18" fill="none" stroke="var(--green)" stroke-width="2"/></svg>
    <h3>Bootstrap Alley</h3>
    <p>We cover the entire Asian region and pick the top 10 startups to compete in Arena. The final battle will take place live on the Main stage on Thursday 7 May. Applications are still open!</p>
  </div>
  <div class="feature" style="left:777px;top:290px">
    <svg class="feature-icon" width="56" height="56" viewBox="0 0 56 56"><circle cx="28" cy="28" r="27" fill="var(--white)" stroke="var(--green)" stroke-width="2"/><path d="M18 35l8-9 6 5 7-11" fill="none" stroke="var(--green)" stroke-width="2"/></svg>
    <h3 class="accent">Night Crawl</h3>
    <p>We cover the entire Asian region and pick the top 10 startups to compete in Arena. The final battle will take place live on the Main stage on Thursday 7 May. Applications are still open!</p>
  </div>
</section>

<section class="expect">
  <h2 class="section-title">What to expect at this year's conference</h2>
  <svg class="monitor" width="700" height="520" viewBox="0 0 700 520">
    <defs>
      <linearGradient id="videoTone" x1="0" y1="0" x2="0" y2="1">
        <stop offset="0" stop-color="#6a6a6a"/><stop offset="1" stop-color="#2e2e2e"/>
      </linearGradient>
    </defs>
    <rect x="0" y="0" width="700" height="440" rx="14" fill="#1b1b1b"/>
    <rect x="22" y="22" width="656" height="396" fill="url(#videoTone)" role="img" aria-label="Video still of conference attendees at the exhibition hall"/>
    <circle cx="350" cy="220" r="42" fill="rgba(255,255,255,.85)"/>
    <path d="M337 198v44l36-22z" fill="#333"/>
    <path d="M300 440h100l14 60H286z" fill="#bdbdbd"/>
    <rect x="240" y="498" width="220" height="10" rx="3" fill="#a8a8a8"/>
  </svg>
</section>

<section class="speakers" id="speakers">
  <h2 class="section-title">Speakers</h2>
  <div class="speaker" style="left:140px"><div class="speaker-photo" role="img" aria-label="Speaker portrait"></div><p class="speaker-name">MARCUS LELAND</p><p class="speaker-role">Founder and Group CEO, RideNova</p></div>
  <div class="speaker" style="left:380px"><div class="speaker-photo" role="img" aria-label="Speaker portrait"></div><p class="speaker-name">MARCUS LELAND</p><p class="speaker-role">Founder and Group CEO, RideNova</p></div>
  <div class="speaker" style="left:620px"><div class="speaker-photo" role="img" aria-label="Speaker portrait"></div><p class="speaker-name">MARCUS LELAND</p><p class="speaker-role">Founder and Group CEO, RideNova</p></div>
  <div class="speaker" style="left:860px"><div class="speaker-photo" role="img" aria-label="Speaker portrait"></div><p class="speaker-name">MARCUS LELAND</p><p class="speaker-role">Founder and Group CEO, RideNova</p></div>
  <a class="more-speakers">Click here <em>for more Speakers</em></a>
</section>

<section class="location" id="venue">
  <div class="location-photo" role="img" aria-label="Grey city skyline with bridge"></div>
  <h2 class="location-title">LOCATION</h2>
  <div class="venue-card">
    <h3>Harbourline Convention and Exhibition Centre</h3>
    <p>8 Meridian Quay, Harbourline City<br><br>Singapore 048812</p>
  </div>
  <a class="venue-btn">VENUE DETAILS</a>
</section>

<section class="sponsors" id="sponsors">
  <h2 class="section-title">Platinum Sponsor</h2>
  <div class="sponsor-tabs">
    <span class="active">GOLD SPONSOR</span><span>SILVER SPONSOR</span><span>NIGHT CRAWL SPONSORS</span><span>OFFICIAL NIGHT CRAWL PARTNER</span>
  </div>
  <div class="sponsor-row" style="top:132px">
    <span class="sponsor-mark">Tessaro</span>
    <span class="sponsor-mark">Cloudvane</span>
    <span class="sponsor-mark">Paywell</span>
    <span class="sponsor-mark">Korvex</span>
  </div>
  <div class="sponsor-row" style="top:218px">
    <span class="sponsor-mark"><i></i>Metrics Guild</span>
    <span class="sponsor-mark">Fundbridge</span>
    <span class="sponsor-mark">Asia Ledger Review</span>
    <span class="sponsor-mark"><i></i>RideNova</span>
  </div>
</section>

<footer class="site-footer" id="contact">
  <div class="footer-col" style="left:140px;width:260px">
    <h4>About us</h4>
    <p>Held bi-annually in Singapore, Japan and Australia, NEXORA is Asia's signature conference, showcasing newly launched and product-ready tech startups from across the region.</p>
  </div>
  <div class="footer-col" style="left:470px;width:300px">
    <h4>Recent news</h4>
    <ul>
      <li>Nexora Meets Singapore 2015 – Team Roundup</li>
      <li>Nexora Meets Singapore 2015 – Arena Finalists</li>
      <li>Nexora Meets Singapore 2015 – Night Crawl</li>
      <li>Nexora Meets Singapore 2015 – Speaker List</li>
      <li>Nexora Meets Singapore 2015 – Ticket Update</li>
      <li>Nexora Meets Singapore 2015 – Venue Notes</li>
      <li>Nexora Meets Singapore 2015 – Team Roundup</li>
    </ul>
  </div>
  <div class="footer-col" style="left:860px;width:220px">
    <h4>Get your tickets today</h4>
    <a class="register-btn">Register Now</a>
  </div>
  <p class="copyright">Copyright © 2015 NEXORA. All rights reserved. Terms of use · Privacy Policy</p>
</footer>

</body>
</html>
```